Medical group practice

We need a flyer design incorporating the three doctors in the practice, there is a general practitioner, ophthalmologist and an obstetrician & Gynaecologist. see the attached file for the concept. will leave the colour design up to you

Target Market(s)

general public

Industry/Entity Type

Health Care

Colors

Designer to choose colors to be used in the design.

Requirements
Must have
• logos included in attachement

```html
<!DOCTYPE html>
<html lang="en">
<head>
<meta charset="utf-8">
<title>Brightwell Medical Flyer</title>
<link rel="stylesheet" href="https://fonts.googleapis.com/css2?family=Dosis:wght@400;500;600;800&display=swap">
<style>
:root{
  --page-bg:#d4d4d4;
  --sky:#62c3ea;
  --sky-light:#9fdaf3;
  --card:#e2e2e2;
  --ink-blue:#1b7fb8;
  --ink-navy:#1d2f6e;
  --brand-red:#ea4a4d;
  --white:#ffffff;
}
*{box-sizing:border-box;margin:0;padding:0}
html,body{width:1200px;height:960px;overflow:hidden}
body{background:var(--page-bg);font-family:'Dosis',sans-serif;display:flex;align-items:center;justify-content:center}
.flyer{position:relative;width:740px;height:930px;background:var(--white);overflow:hidden;box-shadow:0 6px 18px rgba(0,0,0,.25)}
.hero{position:absolute;left:0;top:0;width:740px;height:205px;background:#cfd8e0}
.hero .photo{position:absolute;top:0;height:205px}
.photo-gp{left:0;width:300px;background:linear-gradient(135deg,#dfe6ec,#9fb0bf);clip-path:polygon(0 0,100% 0,78% 100%,0 100%)}
.photo-eye{left:190px;width:360px;background:linear-gradient(160deg,#8c99a8,#3f4a58);clip-path:polygon(28% 0,100% 0,86% 100%,0 100%)}
.photo-ob{left:470px;width:270px;background:linear-gradient(135deg,#f2ebe4,#d8b6b0);clip-path:polygon(28% 0,100% 0,100% 100%,0 100%)}
.band{position:absolute;left:0;top:205px;width:740px;height:235px;background:linear-gradient(180deg,var(--sky),var(--sky-light))}
.brand-mark{position:absolute;left:40px;top:228px;width:58px;height:58px;border-radius:50%;background:var(--brand-red)}
.title{position:absolute;left:115px;top:220px;font-size:58px;font-weight:800;color:var(--brand-red);letter-spacing:1px}
.tagline{position:absolute;left:0;width:740px;text-align:center;top:295px;padding-left:80px;font-size:28px;font-weight:600;color:var(--white)}
.hours{position:absolute;left:0;width:740px;text-align:center;top:340px;padding-left:100px;font-size:17px;color:var(--ink-navy)}
.cards{position:absolute;left:28px;top:380px;width:684px;display:flex;gap:18px}
.card{flex:1;height:445px;background:var(--card);border:3px solid var(--white);text-align:center;color:var(--ink-blue);display:flex;flex-direction:column;align-items:stretch;padding:10px 12px 12px}
.logo-slot{height:84px;flex:none;display:flex;align-items:center;justify-content:center;gap:6px}
.logo-square{width:68px;height:68px;background:#1d8fb8;border-radius:6px}
.logo-circle{width:66px;height:66px;border-radius:50%;background:#2a4f9e}
.logo-eye{flex-direction:column}
.logo-eye .dot{width:48px;height:48px;border-radius:50%;background:#6aa8d8}
.logo-eye .name{font-size:13px;font-weight:600;color:#7a2a8a}
.doctor{align-self:center;background:var(--white);color:var(--ink-navy);font-size:16px;padding:2px 6px;margin-top:6px;line-height:1.2}
.doctor.long{font-size:14px}
.role{font-size:17px;margin-top:8px;line-height:1.2}
.role.small{font-size:15px}
.rule{border-top:1px dashed #fff;margin:16px 2px 10px}
.rule.tight{margin:8px 2px 6px}
.services{list-style:none;font-size:19px;line-height:1.35}
.services.mid{font-size:17px;line-height:1.4}
.services.compact{font-size:15px;line-height:1.2}
.services .head{color:var(--ink-navy);font-style:italic}
.email{margin-top:auto;background:var(--white);color:var(--ink-navy);font-size:14px;line-height:1.4;padding:1px 0}
.footer{position:absolute;left:0;bottom:0;width:740px;height:92px;background:var(--sky);color:var(--ink-navy)}
.lines{display:flex;justify-content:space-around;padding-top:10px;font-size:15px;text-align:center;line-height:1.2}
.address{border-top:1px dashed #fff;margin:8px 16px 0;padding-top:6px;text-align:center;font-size:18px}
</style>
</head>
<body>
<div class="flyer">
  <div class="hero">
    <div class="photo photo-gp" role="img" aria-label="Photo of a general practitioner with a tablet talking to a patient"></div>
    <div class="photo photo-eye" role="img" aria-label="Photo of an ophthalmologist with eye examination equipment"></div>
    <div class="photo photo-ob" role="img" aria-label="Photo of an obstetrician with a pregnant patient"></div>
  </div>
  <div class="band"></div>
  <div class="brand-mark"></div>
  <h1 class="title">BRIGHTWELL MEDICAL</h1>
  <p class="tagline">Your Health is our Priority</p>
  <p class="hours">Opening hours : Monday - Fridays 9am-6pm, Saturdays 10am - 5pm</p>

  <div class="cards">
    <section class="card">
      <div class="logo-slot"><span class="logo-square"></span></div>
      <span class="doctor">Dr. Marcus Ellery, MD</span>
      <p class="role">General Practitioner</p>
      <div class="rule"></div>
      <ul class="services">
        <li>General Checks</li><li>Annual Check ups</li><li>Wound Care/Dressings</li><li>Incision &amp; Drainage</li><li>Suturing lacerations</li><li>Pain Injections</li><li>Glucose checks</li><li>Foreign Body Removal</li>
      </ul>
      <p class="email">m.ellery.doc@mailbox.test</p>
    </section>
    <section class="card">
      <div class="logo-slot logo-eye"><span class="dot"></span><span class="name">Clearview Eye Services</span></div>
      <span class="doctor">Dr. Lucia R. Fenwick MD</span>
      <p class="role">Surgeon Ophthalmologist</p>
      <div class="rule"></div>
      <ul class="services mid">
        <li>Eyes disease examination,</li><li>Surgery of Pterygium,</li><li>Cataract,</li><li>Glaucoma,</li><li>Emergency: Conjunctivitis,</li><li>Traumatism,</li><li>Foreign body and more</li>
      </ul>
      <p class="email">lucia.doct@mailbox.test</p>
    </section>
    <section class="card">
      <div class="logo-slot"><span class="logo-circle"></span></div>
      <span class="doctor long">Dr. Anil Rowden, BMedSci,<br>MBBS, DM (O&amp;G), FACOG</span>
      <p class="role small">Obstetrician &amp; Gynaecologist</p>
      <div class="rule tight"></div>
      <ul class="services compact">
        <li class="head">Obstetrics:</li><li>Prenatal Care,</li><li>Delivery,</li><li>Postnatal checks,</li><li>High Risk pregnancy</li>
      </ul>
      <div class="rule tight"></div>
      <ul class="services compact">
        <li class="head">Gynaecology:</li><li>Pap smears,</li><li>Abnormal vaginal bleeding,</li><li>Fibroids, Colposcopy,</li><li>Family planning, Infertility,</li><li>Cancer screening, and more</li>
      </ul>
      <p class="email">docrowden@mailbox.test</p>
    </section>
  </div>

  <footer class="footer">
    <div class="lines">
      <p>General Practitioner<br>(555) 014 2201</p>
      <p>Ophthalmologist<br>(555) 014 2202</p>
      <p>Obstetrician/Gynaecologist<br>(555) 014 2203, (555) 014 2204</p>
    </div>
    <p class="address">42 Harbour Road, Port Alder, Westmere / Tel : (555) 014 3300 / 3301</p>
  </footer>
</div>
</body>
</html>
```